Real Estate Templates in Canva

I need someone to create a robust set of Canva template designs for my real estate company team, to streamline content. I need a catalog for my agents to easily go in and pick from different designs and customize for themselves. The correct candidate can emulate the style found on these sites., and in the attached images. I have also uploaded logos to be used.(https://www.brindlehomegroup.com/) and (https://meetkoravel.com/)

I want a fantastic sharp style that has great color blend and is attractive and matches my brand well.

The correct candidate will have access to my Canva Brand Kit and build templates inside of my account.

Also attached is a screenshot of my main color codes

The types of templates can include, but not be limited to the following:
BOTH DIGITAL FOR SOCIAL MEDIA AND PRINT VERSIONS
Listings flyers
Clients testimonials
market stats
open houses
Realtor Insights
Realtor analysis
sold properties
new listing properties
under contract properties
coming soon properties
Bullet points summarizing key data
Photo of the client at closing
Photo of the client at their home

Property Listing Template:

Description of the property
High-quality images
Key features and amenities
Open House Invitation:

Date, time, and location details
Compelling visuals of the property
Call-to-action for attendance
Just Sold Announcement:

Property details (address, price, etc.)
Celebratory message
Testimonials from satisfied clients
Testimonial Template:

Client testimonial
Photo of the client (with permission)
Brief background or story
Market Update Infographic:

Visual representation of current market trends
Realtor's insights and analysis
Buyer's Guide:

Step-by-step guide for homebuyers
Infographics explaining the buying process
Tips and advice for a successful purchase
Seller's Guide:

Information on preparing a home for sale
Infographics on the selling process
Tips for maximizing property value
Seasonal Greetings Template:

Personalized message for clients
Festive visuals or themes
Wishes for a successful year ahead
Neighborhood Highlight:

Showcase a specific neighborhood
Key attractions, schools, amenities
Testimonials from residents (if available)
Behind-the-Scenes:

Photos or videos of the realtor at work
Personalized messages about the real estate process
Humanizing content to connect with the audience
Infographic: Benefits of Working with a Realtor:

Visual representation of the advantages
Statistics or data supporting the benefits
Clear, concise points for easy consumption
Interactive Polls or Quizzes:

Engage the audience with fun polls
Real estate-related quizzes
Encourage interaction and sharing
Client Appreciation Post:

Thanking clients for their trust
Sharing success stories
Expressing gratitude with visuals
Video Tour Teaser:

Sneak peek of a property tour
Create excitement and anticipation

Target Market(s)

General Population ages 30-70

Requirements
Must have
• 60 plus designs
Nice to have
• 100 plus designs

```html
<!DOCTYPE html>
<html lang="en">
<head>
<meta charset="utf-8">
<title>Brindle Real Estate – Social Banners</title>
<link href="https://fonts.googleapis.com/css2?family=Josefin+Sans:wght@600;700&family=Roboto:ital,wght@0,400;0,700;1,400&display=swap" rel="stylesheet">
<style>
  :root {
    --orange: #f39530;
    --orange-soft: rgba(243, 149, 48, 0.55);
    --ink: #1d1512;
    --white: #ffffff;
    --stage: #8f8d88;
    --stage-light: #a9a7a2;
  }
  * { box-sizing: border-box; margin: 0; padding: 0; }
  html, body { width: 1139px; height: 1200px; overflow: hidden; }
  body {
    background: radial-gradient(ellipse at 50% 45%, var(--stage-light), var(--stage) 75%);
    font-family: "Roboto", Arial, sans-serif;
    color: var(--white);
    position: relative;
  }
  .banner {
    position: absolute;
    left: 92px;
    width: 955px;
    height: 318px;
    overflow: hidden;
    box-shadow: 0 10px 28px rgba(0,0,0,0.45);
  }
  .banner--listing { top: 92px; }
  .banner--open-house { top: 441px; }
  .banner--testimonial { top: 789px; }
  .photo, .shape-layer { position: absolute; inset: 0; width: 100%; height: 100%; }
  .brand {
    position: absolute;
    display: flex;
    align-items: center;
    gap: 6px;
    font-family: "Josefin Sans", sans-serif;
    font-weight: 700;
    font-size: 22px;
    color: var(--orange);
    letter-spacing: 0.5px;
  }
  .brand__dot { width: 36px; height: 36px; border-radius: 50%; background: var(--white); }
  .price-badge {
    position: absolute;
    border-radius: 50%;
    background: var(--orange);
    display: flex; align-items: center; justify-content: center;
    font-family: "Josefin Sans", sans-serif;
    font-weight: 700;
    color: var(--white);
    box-shadow: 0 0 0 12px var(--orange-soft);
  }
  /* listing */
  .listing__price { left: 24px; top: 24px; width: 160px; height: 160px; font-size: 28px; }
  .listing__brand { left: 26px; top: 257px; }
  .listing__info { position: absolute; left: 566px; top: 36px; width: 370px; }
  .listing__title {
    font-family: "Josefin Sans", sans-serif; font-weight: 700;
    font-size: 34px; line-height: 1.18; letter-spacing: 0.5px;
  }
  .listing__desc { margin-top: 12px; font-size: 14px; line-height: 1.45; }
  .features {
    margin-top: 18px;
    display: grid; grid-template-columns: 158px 1fr; row-gap: 16px;
    font-size: 14.5px; list-style: none;
  }
  .features li { display: flex; align-items: center; gap: 9px; height: 20px; }
  .features svg { width: 17px; height: 17px; fill: var(--orange); flex: none; }
  /* open house */
  .open__brand { left: 26px; top: 36px; }
  .open__price { left: 278px; top: 53px; width: 76px; height: 76px; font-size: 15px; box-shadow: 0 0 0 12px var(--orange-soft); }
  .open__address {
    position: absolute; left: 27px; top: 116px;
    display: flex; gap: 12px;
    font-family: "Josefin Sans", sans-serif; font-weight: 700;
    font-size: 17px; line-height: 1.6; letter-spacing: 0.5px;
  }
  .open__when {
    position: absolute; left: 27px; top: 180px;
    display: flex; align-items: center; gap: 10px;
    font-family: "Josefin Sans", sans-serif; font-weight: 700; font-size: 17px;
  }
  .open__when svg { width: 18px; height: 18px; }
  .open__when .gap { width: 6px; }
  .cta {
    position: absolute; left: 27px; top: 239px;
    width: 130px; height: 43px; border-radius: 22px;
    background: var(--orange);
    display: flex; align-items: center; justify-content: center;
    font-family: "Josefin Sans", sans-serif; font-weight: 700; font-size: 14px; letter-spacing: 0.8px;
  }
  /* testimonial */
  .testimonial__brand { left: 22px; top: 20px; }
  .testimonial__heading {
    position: absolute; left: 0; right: 0; top: 16px; text-align: center;
    font-family: "Josefin Sans", sans-serif; font-weight: 700; font-size: 36px; letter-spacing: 1px;
  }
  .testimonial__quote {
    position: absolute; left: 165px; width: 625px; top: 177px;
    text-align: center; font-style: italic; font-size: 14.6px; line-height: 20.4px;
  }
  .testimonial__name {
    position: absolute; left: 0; right: 0; top: 275px; text-align: center;
    font-weight: 700; font-size: 17px;
  }
</style>
</head>
<body>

<section class="banner banner--listing">
  <svg class="photo" role="img" aria-label="Photo of a two-storey house with porch lights among autumn trees at sunset" viewBox="0 0 955 318" preserveAspectRatio="none">
    <defs>
      <linearGradient id="autumn" x1="0" y1="0" x2="0" y2="1">
        <stop offset="0" stop-color="#c79a5a"/>
        <stop offset="0.35" stop-color="#8a6a3e"/>
        <stop offset="0.6" stop-color="#4c4a34"/>
        <stop offset="1" stop-color="#4b5a26"/>
      </linearGradient>
    </defs>
    <rect width="955" height="318" fill="url(#autumn)"/>
  </svg>
  <svg class="shape-layer" viewBox="0 0 1500 500" preserveAspectRatio="none">
    <polygon points="831,0 645,265 831,500" fill="var(--orange)"/>
    <polygon points="831,0 1500,0 1500,500 831,500 735,265" fill="var(--ink)"/>
  </svg>
  <div class="price-badge listing__price">$640,000</div>
  <div class="brand listing__brand"><span class="brand__dot"></span>BRINDLE</div>
  <div class="listing__info">
    <h1 class="listing__title">42 W LARCH COURT<br>ALDER SPRINGS, CO</h1>
    <p class="listing__desc">Sed ut perspiciatis unde omnis iste natus error sit voluptatem accusantium</p>
    <ul class="features">
      <li><svg viewBox="0 0 20 20"><rect x="4" y="2" width="12" height="8" rx="1"/><rect x="2" y="11" width="16" height="4"/><rect x="2" y="15" width="2" height="3"/><rect x="16" y="15" width="2" height="3"/></svg>3 BEDROOMS</li>
      <li><svg viewBox="0 0 20 20"><rect x="3" y="2" width="3" height="8"/><rect x="2" y="10" width="16" height="5" rx="2"/><rect x="5" y="15" width="2" height="3"/><rect x="13" y="15" width="2" height="3"/></svg>2.00 BATHROOMS</li>
      <li><svg viewBox="0 0 20 20"><path d="M4 5h12l2 6v5h-3v-2H5v2H2v-5z"/></svg>3 GARAGE</li>
      <li><svg viewBox="0 0 20 20"><path d="M10 2l8 7h-2v9H4V9H2z"/></svg>345 SQ. FEET</li>
      <li><svg viewBox="0 0 20 20" fill="none" stroke="var(--orange)" stroke-width="1.6" style="fill:none"><rect x="2" y="2" width="16" height="16"/><path d="M2 7.3h16M2 12.6h16M7.3 2v16M12.6 2v16"/></svg>0.560 ACRES</li>
      <li><svg viewBox="0 0 20 20"><path d="M2 4h16v14H2z M4 8v8h12V8z"/><rect x="5" y="2" width="2" height="4"/><rect x="13" y="2" width="2" height="4"/><rect x="6" y="10" width="2" height="2"/><rect x="9" y="10" width="2" height="2"/><rect x="12" y="10" width="2" height="2"/><rect x="6" y="13" width="2" height="2"/><rect x="9" y="13" width="2" height="2"/></svg>1986</li>
    </ul>
  </div>
</section>

<section class="banner banner--open-house">
  <svg class="photo" role="img" aria-label="Aerial photo of a wooden house with green metal roof in a pine forest" viewBox="0 0 955 318" preserveAspectRatio="none">
    <defs>
      <linearGradient id="pines" x1="0" y1="0" x2="1" y2="1">
        <stop offset="0" stop-color="#3f5a34"/>
        <stop offset="0.45" stop-color="#6f6a45"/>
        <stop offset="1" stop-color="#3c5f2c"/>
      </linearGradient>
    </defs>
    <rect width="955" height="318" fill="url(#pines)"/>
  </svg>
  <svg class="shape-layer" viewBox="0 0 1500 500" preserveAspectRatio="none">
    <defs>
      <linearGradient id="shade" x1="0" y1="0" x2="0" y2="1">
        <stop offset="0" stop-color="#1f2a1c"/>
        <stop offset="1" stop-color="#1a1a18"/>
      </linearGradient>
    </defs>
    <path d="M0 0H420Q665 250 420 500H0Z" fill="var(--orange)"/>
    <path d="M0 0H395Q640 250 395 500H0Z" fill="url(#shade)" opacity="0.96"/>
  </svg>
  <div class="brand open__brand"><span class="brand__dot"></span>BRINDLE</div>
  <div class="price-badge open__price">$610,000</div>
  <div class="open__address">
    <svg width="24" height="26" viewBox="0 0 24 26"><path d="M12 1a9 9 0 0 0-9 9c0 7 9 15 9 15s9-8 9-15a9 9 0 0 0-9-9z" fill="var(--orange)"/><circle cx="12" cy="10" r="3.5" fill="#1f2a1c"/></svg>
    <p>215 TIMBER RIDGE<br>ALDER SPRINGS, CO</p>
  </div>
  <div class="open__when">
    <svg viewBox="0 0 20 20" fill="none" stroke="var(--orange)" stroke-width="1.8"><rect x="2" y="4" width="16" height="14"/><path d="M6 2v4M14 2v4M2 8h16M6 11h2M10 11h2M14 11h1M6 14h2M10 14h2"/></svg>
    <span>Dec 02,2023</span>
    <span class="gap"></span>
    <svg viewBox="0 0 20 20" fill="none" stroke="var(--orange)" stroke-width="2"><circle cx="10" cy="10" r="8"/><path d="M10 5v5h4"/></svg>
    <span>02:00PM</span>
  </div>
  <div class="cta">GET DETAILS</div>
</section>

<section class="banner banner--testimonial">
  <svg class="photo" role="img" aria-label="Aerial photo of a dense pine forest with scattered homes" viewBox="0 0 955 318" preserveAspectRatio="none">
    <defs>
      <linearGradient id="canopy" x1="0" y1="0" x2="1" y2="1">
        <stop offset="0" stop-color="#2e3a26"/>
        <stop offset="0.5" stop-color="#3b4530"/>
        <stop offset="1" stop-color="#2a3422"/>
      </linearGradient>
    </defs>
    <rect width="955" height="318" fill="url(#canopy)"/>
  </svg>
  <svg class="shape-layer" viewBox="0 0 955 318">
    <circle cx="478" cy="-70" r="191" fill="var(--orange)"/>
    <circle cx="478" cy="115" r="52" fill="var(--orange)"/>
    <circle cx="478" cy="115" r="46" fill="#6c7f95" role="img" aria-label="Portrait of the client"/>
  </svg>
  <div class="brand testimonial__brand"><span class="brand__dot"></span>BRINDLE</div>
  <h2 class="testimonial__heading">TESTIMONIALS</h2>
  <p class="testimonial__quote">"This team is second to none. So kind to us and such huge advocates for their clients. We purchased a home with them and had a wonderful experience. Even during this time of great uncertainty and chaos they kept us calm and always easy to communicate with. We truly feel like we gained close friends through this process."</p>
  <p class="testimonial__name">Marla Quinlan</p>
</section>

</body>
</html>
```